Insert card for anti-slip sticker

Product packaging should be inspired by the following
packaging and stand out at the same time: https://shopr.example/7QvKtwe

The packaging is not packaging in the conventional sense, but rather a kind of insert card that can be opened.
This can also be found in the linked product.

On the front of the card: Product name (20 anti-slip strips), advantages of the product and a appealing picture with the product

Inside: Instructions for use and product tips

Back: Images with possible uses, company headquarters, email for contact purposes, note about positive evaluation on Vendaro

```html
<!DOCTYPE html>
<html lang="de">
<head>
<meta charset="utf-8">
<title>Anti-Rutsch Streifen – Einlegekarte</title>
<link href="https://fonts.googleapis.com/css2?family=Cormorant+Garamond:wght@300;400;500&family=Jost:wght@300;400;500;600&display=swap" rel="stylesheet">
<style>
:root{
  --stage:#6b6c70;
  --paper:#f6f6f4;
  --gold:#c9a349;
  --ink:#1d1d1d;
  --ink-soft:#333;
  --dark:#141414;
}
*{box-sizing:border-box;margin:0;padding:0}
html,body{width:1200px;height:924px;overflow:hidden;background:var(--stage)}
body{position:relative;font-family:"Jost",sans-serif;color:var(--ink)}
.label{position:absolute;top:121px;font-family:"Cormorant Garamond",serif;font-size:9px;letter-spacing:.6px;color:#fff}
.spread{position:absolute;top:138px;width:449px;height:671px;overflow:hidden;background:var(--paper);box-shadow:0 6px 14px rgba(0,0,0,.45)}
.spread-outer{left:123px}
.spread-inner{left:642px}
.art{position:absolute;left:0;top:0}
.abs{position:absolute}
.title{position:absolute;display:flex;align-items:center;gap:7px}
.title-num{font-family:"Cormorant Garamond",serif;font-weight:300;font-size:50px;line-height:1;color:var(--gold);letter-spacing:2px}
.title-rule{width:1px;height:33px;background:#444}
.title-words{font-family:"Cormorant Garamond",serif;color:var(--gold);line-height:1.05}
.title-words .small{display:block;font-size:13px;letter-spacing:.8px}
.title-words .big{display:block;font-size:19px;letter-spacing:1.2px}
.pill{position:absolute;border:1px solid var(--gold);border-radius:10px;text-align:center;font-size:7.5px;letter-spacing:.5px;background:#fff;color:var(--ink)}
.feedback{position:absolute;border:1px solid var(--gold);border-radius:6px;background:#fff;text-align:center;font-size:6.6px;line-height:9.5px;font-weight:300;padding-top:7px}
.note{position:absolute;text-align:center;font-size:6.6px;line-height:9.8px;font-weight:300}
.origin{position:absolute;font-family:"Cormorant Garamond",serif;font-size:8.5px;letter-spacing:.6px;color:var(--gold);text-align:center}
.company{position:absolute;left:15px;top:599px;font-size:7.8px;line-height:10.4px;font-weight:300;color:#fff}
.mail{position:absolute;left:15px;top:646px;display:flex;align-items:center;gap:6px;font-size:7.8px;color:#fff}
.mail-dot{width:12px;height:12px;border-radius:50%;border:1px solid var(--gold)}
.feature{position:absolute;width:70px;text-align:center}
.feature-icon{display:flex;width:52px;height:52px;margin:0 auto;border-radius:50%;background:#0e0e0e;border:2px solid #fff;align-items:center;justify-content:center}
.feature-name{display:block;margin-top:3px;font-size:6.4px;font-weight:600;line-height:8.5px;color:#fff;letter-spacing:.3px}
.guide-head{position:absolute;left:18px;top:133px;font-family:"Cormorant Garamond",serif;font-weight:500;font-size:13.5px;letter-spacing:1px}
.step-text{position:absolute;left:18px;width:190px;font-size:7.3px;line-height:11.1px;font-weight:300;color:var(--ink-soft)}
.step-text b{font-weight:300;color:var(--gold)}
.step-text i{font-style:italic}
.step-photo{position:absolute;width:78px;height:78px;border-radius:50%;border:2px solid var(--gold)}
.step-num{position:absolute;width:25px;height:25px;border-radius:50%;background:#0d0d0d;border:1.5px solid #fff;color:#fff;font-size:11px;font-weight:300;display:flex;align-items:center;justify-content:center}
.step-label{position:absolute;left:349px;width:95px;font-size:10.2px;line-height:12.6px;font-weight:300;color:var(--ink)}
.step-title{display:block;color:var(--gold);font-weight:400}
</style>
</head>
<body>

<span class="label" style="left:136px">BACK</span>
<span class="label" style="left:402px">FRONT</span>
<span class="label" style="left:654px">INSIDE LEFT</span>
<span class="label" style="left:920px">INSIDE RIGHT</span>

<section class="spread spread-outer">
  <svg class="art" width="449" height="671" viewBox="0 0 449 671">
    <defs>
      <linearGradient id="legsTone" x1="0" y1="0" x2="1" y2="0">
        <stop offset="0" stop-color="#5d5d5d"/>
        <stop offset=".35" stop-color="#8f8f8f"/>
        <stop offset=".6" stop-color="#a07b62"/>
        <stop offset=".8" stop-color="#6a5a52"/>
        <stop offset="1" stop-color="#1c1c1c"/>
      </linearGradient>
      <linearGradient id="rainTone" x1="0" y1="0" x2="0" y2="1">
        <stop offset="0" stop-color="#8a8a8a"/>
        <stop offset=".45" stop-color="#b9b6b2"/>
        <stop offset=".7" stop-color="#c99d82"/>
        <stop offset="1" stop-color="#1e1e1e"/>
      </linearGradient>
      <linearGradient id="foldShade" x1="0" y1="0" x2="1" y2="0">
        <stop offset="0" stop-color="#fff" stop-opacity="0"/>
        <stop offset="1" stop-color="#bdbdbd" stop-opacity=".7"/>
      </linearGradient>
      <linearGradient id="backFoot" x1="0" y1="0" x2="1" y2="1">
        <stop offset="0" stop-color="#0e0e0e"/>
        <stop offset=".6" stop-color="#2a2a2a"/>
        <stop offset="1" stop-color="#4a4a4a"/>
      </linearGradient>
      <linearGradient id="frontFoot" x1="0" y1="0" x2="0" y2="1">
        <stop offset="0" stop-color="#333"/>
        <stop offset="1" stop-color="#050505"/>
      </linearGradient>
      <linearGradient id="circA" x1="0" y1="0" x2="1" y2="1"><stop offset="0" stop-color="#e9e6e2"/><stop offset=".6" stop-color="#c9a898"/><stop offset="1" stop-color="#9a9a9a"/></linearGradient>
      <linearGradient id="circB" x1="0" y1="0" x2="1" y2="1"><stop offset="0" stop-color="#d9d9d9"/><stop offset=".5" stop-color="#8b8c8e"/><stop offset=".7" stop-color="#d6a98b"/><stop offset="1" stop-color="#6d6e70"/></linearGradient>
      <linearGradient id="circC" x1="0" y1="0" x2="1" y2="1"><stop offset="0" stop-color="#8a7a6a"/><stop offset=".5" stop-color="#e8e2d6"/><stop offset="1" stop-color="#c2a57e"/></linearGradient>
    </defs>

    <path d="M150 0 C170 80 215 170 228 240 V671 H205 C212 500 215 300 150 0 Z" fill="url(#foldShade)"/>

    <!-- front photo -->
    <path role="img" aria-label="Foto: Beine unter der Dusche auf Anti-Rutsch-Streifen" d="M179 0 H449 V414 Q342 544 228 462 V235 C224 150 202 70 179 0 Z" fill="url(#rainTone)"/>
    <path d="M179 0 H449 V225 Q330 200 205 40 C197 25 188 12 179 0 Z" fill="url(#legsTone)"/>
    <path d="M198 28 Q300 190 449 222" fill="none" stroke="var(--gold)" stroke-width="3"/>
    <path d="M228 671 V651 Q330 600 449 606 V671 Z" fill="url(#frontFoot)"/>

    <!-- back images -->
    <circle role="img" aria-label="Foto: Hand bringt einen Streifen an" cx="60" cy="170" r="36" fill="url(#circA)" stroke="var(--gold)" stroke-width="1.5"/>
    <circle role="img" aria-label="Foto: Fuß auf Streifen in der Duschwanne" cx="122" cy="217" r="59" fill="url(#circB)" stroke="var(--gold)" stroke-width="1.5"/>
    <circle role="img" aria-label="Foto: Streifen auf einer Holztreppe" cx="167" cy="282" r="36" fill="url(#circC)" stroke="var(--gold)" stroke-width="1.5"/>

    <line x1="72" y1="384" x2="158" y2="384" stroke="#c4c4c4" stroke-width=".6"/>
    <line x1="72" y1="527" x2="158" y2="527" stroke="#c4c4c4" stroke-width=".6"/>
    <text x="92" y="411" font-size="8" fill="#f0a020" font-family="Jost, sans-serif" letter-spacing="1">★★★★★</text>

    <path d="M0 562 Q150 560 250 671 H0 Z" fill="url(#backFoot)"/>
    <path d="M0 556 Q155 553 258 671" fill="none" stroke="#6a6a6a" stroke-width="4"/>
  </svg>

  <div class="title" style="left:35px;top:83px">
    <span class="title-num">20</span><span class="title-rule"></span>
    <span class="title-words"><span class="small">ANTI-RUTSCH</span><span class="big">STREIFEN</span></span>
  </div>
  <div class="pill" style="left:33px;top:342px;width:162px;height:19px;line-height:17px">BAD / DUSCHE / WANNE / TREPPE</div>
  <div class="feedback" style="left:15px;top:423px;width:197px;height:36px">SIE SIND ZUFRIEDEN? DANN SAGEN SIE ES WEITER.<br>NICHT ZUFRIEDEN? DANN SAGEN SIE ES UNS...</div>
  <p class="note" style="left:24px;top:479px;width:182px">WIR SIND STETIG DARAN UNSERE PRODUKTE ZU VERBESSERN, INDEM SIE FEEDBACK GEBEN HELFEN SIE UNS DABEI.</p>
  <p class="origin" style="left:60px;top:544px;width:110px">MADE IN CHINA</p>
  <p class="company">K&amp;M Haushaltswaren UG<br>(haftungsbeschränkt)<br>Lindenhofweg 14<br>71034 Waldbrunn</p>
  <p class="mail"><span class="mail-dot"></span>kontakt@km-haushaltswaren.example</p>

  <div class="feature" style="left:230px;top:230px">
    <span class="feature-icon"><svg width="28" height="28" viewBox="0 0 28 28"><circle cx="16" cy="6" r="2.3" fill="#fff"/><path d="M9 10 L16 9 L13 16 L18 20 M13 16 L8 20 M16 9 L20 13" stroke="#fff" stroke-width="2" fill="none" stroke-linecap="round"/><line x1="4" y1="24" x2="24" y2="4" stroke="var(--gold)" stroke-width="2"/></svg></span>
    <span class="feature-name">100% Rutschfest</span>
  </div>
  <div class="feature" style="left:230px;top:304px">
    <span class="feature-icon"><svg width="28" height="28" viewBox="0 0 28 28"><path d="M13 3 C10 8 9 10 9 12 a4 4 0 0 0 8 0 C17 10 16 8 13 3Z" fill="#fff"/><path d="M5 18 l5 5 l12 -9" stroke="#fff" stroke-width="1.8" fill="none"/><path d="M18 13 l4 1 l-1 4" stroke="var(--gold)" stroke-width="1.6" fill="none"/></svg></span>
    <span class="feature-name">Wasserdicht</span>
  </div>
  <div class="feature" style="left:230px;top:378px">
    <span class="feature-icon"><svg width="28" height="28" viewBox="0 0 28 28"><rect x="8" y="10" width="13" height="12" rx="2" fill="#fff"/><path d="M6 4 l1 2 l2 1 l-2 1 l-1 2 l-1 -2 l-2 -1 l2 -1z M21 3 l1 2 l2 1 l-2 1 l-1 2 l-1 -2 l-2 -1 l2 -1z" fill="#fff"/></svg></span>
    <span class="feature-name">Komfortable<br>Anwendung</span>
  </div>

  <div class="title" style="left:275px;top:521px">
    <span class="title-num" style="font-size:46px">20</span><span class="title-rule" style="height:30px"></span>
    <span class="title-words"><span class="small">ANTI-RUTSCH</span><span class="big">STREIFEN</span></span>
  </div>
  <div class="pill" style="left:246px;top:569px;width:183px;height:20px;line-height:18px;font-size:8.5px">BAD / DUSCHE / WANNE / TREPPE</div>
</section>

<section class="spread spread-inner">
  <svg class="art" width="449" height="671" viewBox="0 0 449 671">
    <defs>
      <linearGradient id="greyBand" x1="0" y1="0" x2="1" y2="0"><stop offset="0" stop-color="#cfcfcf"/><stop offset="1" stop-color="#8c8c8c"/></linearGradient>
      <linearGradient id="bathTone" x1="0" y1="0" x2="1" y2="1">
        <stop offset="0" stop-color="#7b7873"/><stop offset=".35" stop-color="#a88456"/>
        <stop offset=".65" stop-color="#c08f4f"/><stop offset="1" stop-color="#5e3f1d"/>
      </linearGradient>
      <linearGradient id="floorTone" x1="0" y1="0" x2="1" y2="1">
        <stop offset="0" stop-color="#bcbcbc"/><stop offset=".5" stop-color="#e9e9e8"/><stop offset="1" stop-color="#a9a9a9"/>
      </linearGradient>
      <linearGradient id="cornerTone" x1="0" y1="0" x2="1" y2="0">
        <stop offset="0" stop-color="#d0d0d0"/><stop offset="1" stop-color="#101010"/>
      </linearGradient>
      <linearGradient id="innerFold" x1="0" y1="0" x2="1" y2="0">
        <stop offset="0" stop-color="#fff" stop-opacity="0"/><stop offset="1" stop-color="#b5b5b5" stop-opacity=".75"/>
      </linearGradient>
      <radialGradient id="stepTone" cx=".4" cy=".4" r=".7">
        <stop offset="0" stop-color="#f0ece8"/><stop offset=".45" stop-color="#c9b3a3"/><stop offset=".8" stop-color="#3a3a3a"/><stop offset="1" stop-color="#111"/>
      </radialGradient>
    </defs>

    <rect x="150" y="0" width="74" height="671" fill="url(#innerFold)"/>
    <path d="M95 0 Q150 40 224 62 V0 Z" fill="url(#greyBand)"/>
    <line x1="18" y1="125" x2="192" y2="125" stroke="var(--gold)" stroke-width=".8"/>

    <path role="img" aria-label="Foto: nackte Füße auf Anti-Rutsch-Streifen in heller Duschwanne" d="M0 512 Q210 532 345 671 H0 Z" fill="url(#floorTone)"/>
    <path d="M0 504 Q215 522 355 671" fill="none" stroke="#333" stroke-width="8"/>

    <path role="img" aria-label="Foto: modernes Bad mit Glasdusche und Holzboden" d="M224 0 H449 V250 Q420 285 384 282 Q300 280 224 241 Z" fill="url(#bathTone)"/>
    <path d="M224 99 Q340 130 449 158" fill="none" stroke="var(--gold)" stroke-width="3"/>
    <circle cx="393" cy="227" r="46" fill="none" stroke="#fff" stroke-width="2.5"/>

    <path d="M262 671 Q330 622 449 606 V671 Z" fill="url(#cornerTone)"/>
    <path d="M262 669 Q330 618 449 603" fill="none" stroke="var(--gold)" stroke-width="2"/>

    <circle role="img" aria-label="Foto: Hände nehmen einen Streifen" cx="291" cy="324" r="39" fill="url(#stepTone)" stroke="var(--gold)" stroke-width="2"/>
    <circle role="img" aria-label="Foto: Rückseite des Streifens wird abgezogen" cx="287" cy="436" r="39" fill="url(#stepTone)" stroke="var(--gold)" stroke-width="2"/>
    <circle role="img" aria-label="Foto: Streifen wird auf die Fläche geklebt" cx="289" cy="555" r="39" fill="url(#stepTone)" stroke="var(--gold)" stroke-width="2"/>
  </svg>

  <div class="title" style="left:18px;top:84px">
    <span class="title-num" style="font-size:44px">20</span><span class="title-rule" style="height:30px"></span>
    <span class="title-words"><span class="small">ANTI-RUTSCH</span><span class="big">STREIFEN</span></span>
  </div>
  <h2 class="guide-head">GEBRAUCHSANWEISUNG:</h2>
  <p class="step-text" style="top:157px"><b>1.</b> Um einen optimalen Halt zu erlangen, reinigen Sie hierfür gründlich die Oberfläche, auf welche Sie die Klebestreifen anbringen wollen und lassen Sie diese trocknen.</p>
  <p class="step-text" style="top:212px"><b>2.</b> Lassen Sie zwischen den Klebestreifen einen ausreichenden Platz von 1-3 cm.</p>
  <p class="step-text" style="top:245px"><b>3.</b> Ziehen Sie die Klebestreifen-Rückseite vorsichtig ab. Kleben Sie nun den Streifen auf die gewünschte Fläche.</p>
  <p class="step-text" style="top:290px"><b>4.</b> Drücken Sie den Streifen mit ein wenig Druck fest. Vermeiden Sie erneutes Ablösen und Aufkleben.</p>
  <p class="step-text" style="top:334px"><b>5.</b> Um einen Klebestreifen wieder zu entfernen, erwärmen Sie zunächst den Streifen mit bspw. einem Föhn.</p>
  <p class="step-text" style="top:379px"><b>6.</b> Nun können Sie mit einem Gegenstand (z.B. Schaber, Spachtel) unter eine Ecke des Streifens gehen. Heben Sie diesen nun vorsichtig an und ziehen Sie den Streifen langsam ab.</p>
  <p class="step-text" style="top:434px"><b>7.</b> Falls auf der Oberfläche noch Rückstände sein sollten, entfernen Sie diese einfach mit etwas Oberflächenreiniger.</p>
  <p class="step-text" style="top:475px"><b>Tipp:</b> <i>Nicht auf unebenen oder strukturierten Oberflächen anbringen.</i></p>

  <span class="step-num" style="left:308px;top:297px">1</span>
  <span class="step-num" style="left:312px;top:402px">2</span>
  <span class="step-num" style="left:310px;top:525px">3</span>
  <p class="step-label" style="top:312px"><span class="step-title">SCHRITT 1</span>Nehmen Sie einen Streifen</p>
  <p class="step-label" style="top:419px"><span class="step-title">SCHRITT 2</span>Entfernen Sie die Rückseite</p>
  <p class="step-label" style="top:523px"><span class="step-title">SCHRITT 3</span>Bringen Sie den Streifen auf der gewünschten Fläche an</p>
</section>

</body>
</html>
```